An anniversary gift for my girlfriend

My girlfriend and I have been dating for almost 2 years. We met online and this has afforded us the really unique opportunity to have the first words we said to each other (the whole conversation, in fact) preserved. We're moving in together in a few months and she doesn't know that I saved the conversation. I've been waiting for this to turn it into something we can hang in our new place.

The only phrase I want to use is:
"Well if you dislike people's knees then I think we'll get along famously"

It's an Nobody Leaves Before Midnight in Portland reference for the curious.

I want the poster to use the words themselves as the art; I'm thinking typography. I'd like it to match her aesthetic, she likes to wear Nora Vell and T. Brisk. Colors shouldn't be anything too "girly". Somewhere I'd like to include the date June 1, 2015. It shouldn't be a major piece of the poster though, just a way to denote the date.

It should fit (and be fully visible in) a 16x20 (inches) frame

Thanks in advance for the work!

Requirements
Must have
• Must use only the words: "Well if you dislike people's knees then I think we'll get along famously"
• I want this to be typography, so making the phrase the center of the poster and the art itself.

```html
<!DOCTYPE html>
<html lang="en">
<head>
<meta charset="utf-8">
<title>Well If You Dislike People's Knees — Anniversary Poster</title>
<link rel="stylesheet" href="https://fonts.googleapis.com/css2?family=Comfortaa:wght@700&family=Yesteryear&family=Montserrat:wght@800;900&family=Kalam:wght@400&family=Cinzel:wght@400&family=Rye&family=Raleway:wght@500&display=swap">
<style>
  :root {
    --paper: #f7f7f7;
    --paper-edge: #ececec;
    --denim: #5a76bb;
    --apricot: #f4a25c;
    --lagoon: #47bfd1;
    --lime: #96c64a;
    --raspberry: #d9355f;
    --mustard: #e2d12d;
    --teal: #5ec8d6;
    --orange: #f5a55a;
    --green: #9ccb4f;
    --navy: #2f3c8f;
    --sky: #3aa9d8;
  }
  html, body {
    margin: 0;
    padding: 0;
    width: 1036px;
    height: 1200px;
    overflow: hidden;
  }
  body {
    background: radial-gradient(ellipse at center, var(--paper) 55%, var(--paper-edge) 100%);
  }
  .poster { display: block; width: 1036px; height: 1200px; }
  .line-well { font-family: "Comfortaa", sans-serif; font-weight: 700; font-size: 84px; fill: var(--denim); }
  .line-you { font-family: "Yesteryear", cursive; font-size: 200px; fill: var(--apricot); }
  .line-people { font-family: "Montserrat", sans-serif; font-weight: 800; font-size: 84px; fill: var(--lagoon); }
  .line-people .small { font-size: 60px; }
  .line-then { font-family: "Kalam", cursive; font-size: 120px; fill: var(--lime); }
  .line-get { font-family: "Cinzel", serif; font-size: 146px; fill: var(--raspberry); }
  .along { font-family: "Montserrat", sans-serif; font-weight: 900; font-size: 186px; }
  .along-a { fill: var(--mustard); }
  .along-l { fill: var(--teal); }
  .along-o { fill: var(--orange); }
  .along-n { fill: var(--green); }
  .along-g { fill: var(--navy); }
  .line-famously { font-family: "Rye", serif; font-size: 214px; }
  .ink-navy { fill: var(--navy); }
  .ink-pink { fill: var(--raspberry); }
  .date-rule { stroke: var(--sky); stroke-width: 1.2; }
  .date { font-family: "Raleway", sans-serif; font-weight: 500; font-size: 19px; letter-spacing: 4px; fill: var(--sky); }
</style>
</head>
<body>
<svg class="poster" viewBox="0 0 1036 1200" xmlns="http://www.w3.org/2000/svg" aria-label="Well if you dislike people's knees then I think we'll get along famously — June 1, 2015">
  <text class="line-well" x="94" y="114" textLength="346" lengthAdjust="spacingAndGlyphs">well if</text>
  <text class="line-you" x="72" y="268" textLength="864" lengthAdjust="spacingAndGlyphs">you dislike</text>
  <text class="line-people" x="156" y="374" textLength="762" lengthAdjust="spacingAndGlyphs">PEOPLE'S KN<tspan class="small">ees</tspan></text>
  <text class="line-then" x="206" y="534" textLength="644" lengthAdjust="spacingAndGlyphs">then i think...</text>
  <text class="line-get" x="144" y="682" textLength="750" lengthAdjust="spacingAndGlyphs">WE'LL GET</text>

  <g class="along">
    <text class="along-a" x="174" y="858" textLength="132" lengthAdjust="spacingAndGlyphs">A</text>
    <text class="along-l" x="316" y="898" textLength="92" lengthAdjust="spacingAndGlyphs">L</text>
    <text class="along-o" x="414" y="858" textLength="138" lengthAdjust="spacingAndGlyphs">O</text>
    <text class="along-n" x="570" y="898" textLength="120" lengthAdjust="spacingAndGlyphs">N</text>
    <text class="along-g" x="700" y="840" textLength="140" lengthAdjust="spacingAndGlyphs">G</text>
  </g>

  <text class="line-famously" x="50" y="1094" textLength="934" lengthAdjust="spacingAndGlyphs"><tspan class="ink-navy">F</tspan><tspan class="ink-pink">A</tspan><tspan class="ink-navy">M</tspan><tspan class="ink-pink">O</tspan><tspan class="ink-navy">U</tspan><tspan class="ink-pink">S</tspan><tspan class="ink-navy">L</tspan><tspan class="ink-pink">Y</tspan></text>

  <line class="date-rule" x1="408" y1="1138" x2="600" y2="1138"/>
  <text class="date" x="504" y="1164" text-anchor="middle">JUNE 1, 2015</text>
  <line class="date-rule" x1="408" y1="1176" x2="600" y2="1176"/>
</svg>
</body>
</html>
```